Velmar Computers Brochure design

We need an brochure, in a4 size, it should be 8 pages in total.

We have 9 topics we need covered:
Front page
Velmar introduction
Velmar office series
Velmar Business series
Velmar Performance series
Partners
Oxbrin
Warranty
Contact details, Back page

WE have a new material we want to use instead of the current oxbrin page:

https://www.filecrate-example.com/s/qp7rmxwatg3kzn2/OXBRIN.pdf

• I have added a PowerPoint presentation with information we want in the brochure. There are 9 pages, so if you can merge two of them together to one so we get a total of 8 pages.

I have also added pictures of TQ screens, that can be bundled with all our machines. We also want that to be shown some where, maybe on same page as the computers.

```html
<!DOCTYPE html>
<html lang="en">
<head>
<meta charset="utf-8">
<title>Velmar Computers – Product Brochure</title>
<link rel="stylesheet" href="https://fonts.googleapis.com/css2?family=Open+Sans:wght@600;700;800&display=swap">
<style>
  :root {
    --navy: #1f3b8f;
    --mid-blue: #4e7fc1;
    --pale-blue: #d3d9ec;
    --orange: #f39521;
    --white: #ffffff;
    --grey-text: #6c6c6c;
    --tower-dark: #1c1c1e;
    --tower-light: #4a4a4e;
  }
  * { margin: 0; padding: 0; box-sizing: border-box; }
  html, body {
    width: 848px;
    height: 1200px;
    overflow: hidden;
    background: var(--white);
  }
  .brochure-cover {
    position: relative;
    width: 848px;
    height: 1200px;
    overflow: hidden;
    background: var(--white);
    font-family: "Open Sans", Arial, sans-serif;
  }
  .cover-art {
    position: absolute;
    inset: 0;
    width: 848px;
    height: 1200px;
  }
  .brand-name {
    position: absolute;
    left: 57px;
    top: 78px;
    font-size: 78px;
    font-weight: 800;
    letter-spacing: 1px;
    color: var(--white);
    line-height: 1;
  }
  .cover-title {
    position: absolute;
    left: 57px;
    top: 187px;
    font-size: 26px;
    font-weight: 700;
    color: var(--white);
  }
  .series-list {
    list-style: none;
  }
  .series-item {
    position: absolute;
    left: 20px;
    width: 600px;
    height: 172px;
    display: flex;
    align-items: center;
  }
  .series-item:nth-child(1) { top: 484px; }
  .series-item:nth-child(2) { top: 673px; }
  .series-item:nth-child(3) { top: 862px; }
  .series-badge {
    position: relative;
    width: 172px;
    height: 172px;
    border-radius: 50%;
    background: var(--orange);
    border: 7px solid var(--mid-blue);
    flex: none;
    display: flex;
    align-items: center;
    justify-content: center;
  }
  .series-product {
    width: 62px;
    height: 104px;
    border-radius: 3px;
    background: linear-gradient(135deg, var(--tower-light), var(--tower-dark) 55%);
  }
  .series-name {
    margin-left: 39px;
    font-size: 27px;
    font-weight: 700;
    color: var(--grey-text);
  }
  .cover-year {
    position: absolute;
    left: 730px;
    top: 1115px;
    font-size: 26px;
    font-weight: 700;
    color: var(--white);
  }
</style>
</head>
<body>
<main class="brochure-cover">
  <svg class="cover-art" viewBox="0 0 595 842" preserveAspectRatio="none" aria-hidden="true">
    <path d="M0,0 H595 V214 C450,198 310,226 190,272 C120,298 55,308 0,305 Z" fill="var(--orange)"/>
    <path d="M0,0 H595 V206 C450,190 305,218 185,260 C115,282 55,280 0,274 Z" fill="var(--mid-blue)"/>
    <path d="M0,0 H595 V198 C450,182 300,208 180,246 C110,266 55,258 0,250 Z" fill="var(--pale-blue)"/>
    <path d="M0,0 H595 V190 C450,174 295,198 175,232 C105,250 55,238 0,228 Z" fill="var(--navy)"/>
    <path d="M285,0 C410,22 525,62 600,128" fill="none" stroke="var(--orange)" stroke-width="13"/>
    <path d="M330,0 C445,17 540,52 600,100" fill="none" stroke="var(--mid-blue)" stroke-width="9"/>
    <path d="M380,0 C475,12 552,38 600,72" fill="none" stroke="var(--pale-blue)" stroke-width="8"/>
    <path d="M595,330 C575,540 400,740 95,842 H595 Z" fill="var(--orange)"/>
    <path d="M595,372 C580,570 430,760 190,842 H595 Z" fill="var(--mid-blue)"/>
    <path d="M595,405 C585,590 455,770 245,842 H595 Z" fill="var(--pale-blue)"/>
    <path d="M595,432 C590,610 475,780 290,842 H595 Z" fill="var(--navy)"/>
  </svg>

  <header>
    <div class="brand-name">VELMAR</div>
    <h1 class="cover-title">Product Brochure</h1>
  </header>

  <ul class="series-list">
    <li class="series-item">
      <div class="series-badge"><div class="series-product" role="img" aria-label="Office Series desktop tower computer"></div></div>
      <span class="series-name">Office Series</span>
    </li>
    <li class="series-item">
      <div class="series-badge"><div class="series-product" role="img" aria-label="Business Series desktop tower computer"></div></div>
      <span class="series-name">Business Series</span>
    </li>
    <li class="series-item">
      <div class="series-badge"><div class="series-product" role="img" aria-label="Enterprise Series desktop tower computer"></div></div>
      <span class="series-name">Enterprise Series</span>
    </li>
  </ul>

  <div class="cover-year">2013</div>
</main>
</body>
</html>
```